Corvane Safety 1 page advertising flier needed

Need to show clients (architects) what we do and our services. We provide Fall Protection and Window Cleaning Equipment turnkey services. This is for a 1 e-page online ad. Needs to pop out and show good color and what it is that we do. We have a 24 hour response policy so that will need to be on here as well. Needs to be better than the competitors attached as part of the photos!

Target Market(s)

architects

Industry/Entity Type

Safety

Colors
3277b5
0355a3
ec1f27
ffffff

Requirements
Must have
• Pictures, but not all of them. Whatever you think looks good and goes with our services. Mission Statement somewhere on this ad

```html
<!DOCTYPE html>
<html lang="en">
<head>
<meta charset="utf-8">
<title>Corvane Safety – Flier</title>
<link href="https://fonts.googleapis.com/css2?family=Source+Sans+3:wght@400;600;700;800&family=Oswald:wght@500;600&display=swap" rel="stylesheet">
<style>
  :root {
    --blue: #3277b5;
    --blue-deep: #0355a3;
    --red: #ec1f27;
    --red-deep: #b8121a;
    --white: #ffffff;
    --grey: #4a4a4d;
    --grey-dark: #2f2f31;
    --sky: #c9dcee;
  }
  html, body { margin: 0; padding: 0; background: #e6e6e6; overflow: hidden; }
  .flier {
    position: relative; width: 707px; height: 1200px; overflow: hidden;
    font-family: "Source Sans 3", Arial, sans-serif; color: var(--white);
    background: var(--white);
  }
  .flier__art { position: absolute; inset: 0; }
  .header {
    position: absolute; top: 40px; left: 0; width: 100%;
    display: flex; justify-content: center; align-items: center; gap: 22px;
    font-weight: 700; font-size: 15px; color: var(--blue-deep);
  }
  .brand { display: flex; align-items: center; gap: 7px; font-size: 19px; color: var(--red); }
  .brand__mark { width: 14px; height: 14px; background: var(--blue-deep); }
  .intro { position: absolute; left: 17px; top: 466px; width: 330px; }
  .intro__lead { font-size: 19px; font-weight: 400; line-height: 1; letter-spacing: .3px; }
  .intro__title { font-size: 22px; font-weight: 800; line-height: 1.15; margin: 6px 0 2px; }
  .intro__sub { font-size: 17px; font-weight: 400; }
  .mission__title {
    font-size: 17px; font-weight: 700; margin: 12px 0 0;
    display: inline-block; border-bottom: 2px solid var(--white); padding-bottom: 2px;
  }
  .mission__list { margin: 14px 0 0; padding-left: 14px; font-size: 11.5px; line-height: 1.3; }
  .mission__list li { margin-bottom: 11px; }
  .contact { position: absolute; left: 17px; top: 910px; width: 300px; font-size: 13px; line-height: 1.55; }
  .contact__label { color: var(--red); font-weight: 700; font-size: 16px; letter-spacing: .3px; text-transform: uppercase; }
  .contact__block { margin-bottom: 12px; }
  .contact__fax { color: var(--red); }
  .phone { position: absolute; left: 17px; top: 1100px; display: flex; align-items: center; gap: 10px;
    font-family: "Oswald", Arial, sans-serif; font-weight: 600; font-size: 29px; }
  .web { position: absolute; left: 17px; top: 1150px; display: flex; align-items: center; gap: 10px; font-size: 18px; font-weight: 600; }
  .social { position: absolute; left: 274px; top: 1150px; display: flex; gap: 12px; }
  .social span { width: 24px; height: 24px; border-radius: 50%; background: var(--red); }
  .response { position: absolute; right: 14px; top: 545px; display: flex; align-items: center; gap: 8px; }
  .response__num { font-family: "Oswald", Arial, sans-serif; font-size: 40px; font-weight: 600; color: var(--red); font-style: italic; }
  .response__text { font-size: 15px; font-weight: 700; line-height: 1.05; }
  .services__title {
    position: absolute; right: 14px; top: 610px; font-size: 29px; font-weight: 400; letter-spacing: .5px;
    border-bottom: 2px solid var(--white); padding-bottom: 2px;
  }
  .services__title b { font-weight: 800; }
  .services { position: absolute; right: 12px; top: 680px; margin: 0; padding: 0; list-style: none; }
  .services li {
    display: flex; justify-content: flex-end; align-items: center; gap: 10px;
    font-size: 17px; font-weight: 600; text-align: right; line-height: 1.1; height: 49px;
  }
  .services li.services__item--double { height: 58px; }
  .hex-icon { width: 26px; height: 28px; flex: none; }
</style>
</head>
<body>
<main class="flier">
  <svg class="flier__art" width="707" height="1200" viewBox="0 0 707 1200">
    <defs>
      <linearGradient id="skyFill" x1="0" y1="0" x2="1" y2="1">
        <stop offset="0" stop-color="#eef4fa"/>
        <stop offset=".5" stop-color="#b9d1ea"/>
        <stop offset="1" stop-color="#3f6fa8"/>
      </linearGradient>
      <linearGradient id="redFill" x1="0" y1="0" x2="0" y2="1">
        <stop offset="0" stop-color="#ec1f27"/>
        <stop offset="1" stop-color="#b8121a"/>
      </linearGradient>
      <linearGradient id="blueFill" x1="0" y1="0" x2="0" y2="1">
        <stop offset="0" stop-color="#3277b5"/>
        <stop offset="1" stop-color="#0355a3"/>
      </linearGradient>
      <linearGradient id="greyFill" x1="0" y1="0" x2="0" y2="1">
        <stop offset="0" stop-color="#55555a"/>
        <stop offset="1" stop-color="#2f2f31"/>
      </linearGradient>
      <linearGradient id="photoFill" x1="0" y1="0" x2="0" y2="1">
        <stop offset="0" stop-color="#bcd0e4"/>
        <stop offset="1" stop-color="#55677c"/>
      </linearGradient>
    </defs>
    <rect class="hero-photo" x="0" y="0" width="707" height="820" fill="url(#skyFill)" role="img" aria-label="Photo of a glass office tower against a cloudy sky"/>
    <rect x="0" y="790" width="707" height="410" fill="url(#greyFill)"/>
    <path class="panel-red" d="M0,250 L495,548 Q525,566 512,598 L428,800 Q414,834 378,832 L0,800 Z" fill="url(#redFill)" stroke="#ffffff" stroke-width="4"/>
    <path class="panel-blue" d="M707,318 L707,1200 L300,1200 L256,900 Q248,858 278,830 Z" fill="url(#blueFill)" stroke="#e9eef4" stroke-width="5"/>
    <polygon class="hex-photo" points="100,215 165,258 165,342 100,385 35,342 35,258" fill="url(#photoFill)" stroke="#fff" stroke-width="4" role="img" aria-label="Photo of rooftop davit arms beside a tall tower"/>
    <polygon class="hex-photo" points="250,310 315,353 315,437 250,480 185,437 185,353" fill="url(#photoFill)" stroke="#fff" stroke-width="4" role="img" aria-label="Photo of workers on a suspended window cleaning platform"/>
    <polygon class="hex-photo" points="398,405 463,448 463,532 398,575 333,532 333,448" fill="url(#photoFill)" stroke="#fff" stroke-width="4" role="img" aria-label="Photo of a rooftop fall protection anchor post"/>
  </svg>

  <header class="header">
    <span>Exterior Building</span>
    <span class="brand"><span class="brand__mark"></span>Corvane Safety</span>
    <span>Safety Specialist</span>
  </header>

  <section class="intro">
    <div class="intro__lead">WE PROVIDE</div>
    <div class="intro__title">FALL PROTECTION AND<br>WINDOW CLEANING</div>
    <div class="intro__sub">EQUIPMENT TURNKEY SERVICES</div>
    <div class="mission__title">OUR MISSION</div>
    <ul class="mission__list">
      <li>At Corvane Safety, our mission is to provide a cost effective, safe, and compliant system for accessing the exterior of buildings.</li>
      <li>Corvane Safety is committed to creating long-lasting relationships built on Positive, Responsive Quality Service and reinforced using strong internal teamwork.</li>
      <li>Corvane Safety is committed to our clientele to complete all projects, regardless of adversity faced.</li>
    </ul>
  </section>

  <section class="contact">
    <div class="contact__block">
      <div class="contact__label">Physical Location</div>
      245 Harlow Court, Suite B<br>Brentmoor, CA 94600
    </div>
    <div class="contact__block">
      <div class="contact__label">Mailing Address</div>
      PO Box 41902<br>Ashford Hill, CA 94611<br><span class="contact__fax">Fax:</span> (925) 555-0187
    </div>
  </section>

  <div class="phone">
    <svg width="24" height="24" viewBox="0 0 24 24"><path d="M6 3l3 4-2 2c1 3 4 6 7 7l2-2 4 3-2 4C10 20 4 14 3 5z" fill="#ec1f27"/></svg>
    (800) 555-0142
  </div>
  <div class="web">
    <svg width="22" height="22" viewBox="0 0 22 22"><circle cx="11" cy="11" r="10" fill="#ec1f27"/><circle cx="11" cy="11" r="6" fill="none" stroke="#fff" stroke-width="1.5"/><line x1="5" y1="11" x2="17" y2="11" stroke="#fff" stroke-width="1.5"/></svg>
    www.corvanesafety.com
  </div>
  <div class="social"><span></span><span></span></div>

  <div class="response">
    <span class="response__num">24/7</span>
    <span class="response__text">RESPONSE<br>POLICY</span>
  </div>
  <div class="services__title">OUR <b>SERVICES</b></div>

  <ul class="services">
    <li>Design &amp; Engineering<svg class="hex-icon" viewBox="0 0 26 28"><polygon points="13,1 25,7.5 25,20.5 13,27 1,20.5 1,7.5" fill="#ec1f27" stroke="#fff" stroke-width="1.5"/><circle cx="13" cy="14" r="5" fill="none" stroke="#fff" stroke-width="2"/></svg></li>
    <li>Installation<svg class="hex-icon" viewBox="0 0 26 28"><polygon points="13,1 25,7.5 25,20.5 13,27 1,20.5 1,7.5" fill="#ec1f27" stroke="#fff" stroke-width="1.5"/><path d="M8 14l3 3 7-7" fill="none" stroke="#fff" stroke-width="2"/></svg></li>
    <li>Retrofitting<svg class="hex-icon" viewBox="0 0 26 28"><polygon points="13,1 25,7.5 25,20.5 13,27 1,20.5 1,7.5" fill="#ec1f27" stroke="#fff" stroke-width="1.5"/><path d="M8 19l10-10" stroke="#fff" stroke-width="2.5"/></svg></li>
    <li class="services__item--double">Powered Platforms<br>and Suspension Equipment<svg class="hex-icon" viewBox="0 0 26 28"><polygon points="13,1 25,7.5 25,20.5 13,27 1,20.5 1,7.5" fill="#ec1f27" stroke="#fff" stroke-width="1.5"/><rect x="11" y="7" width="4" height="14" fill="#fff"/></svg></li>
    <li>Fall Protection<svg class="hex-icon" viewBox="0 0 26 28"><polygon points="13,1 25,7.5 25,20.5 13,27 1,20.5 1,7.5" fill="#ec1f27" stroke="#fff" stroke-width="1.5"/><path d="M7 14a6 6 0 0 1 12 0z" fill="#fff"/><line x1="13" y1="14" x2="13" y2="20" stroke="#fff" stroke-width="2"/></svg></li>
    <li>Testing &amp; Certification<svg class="hex-icon" viewBox="0 0 26 28"><polygon points="13,1 25,7.5 25,20.5 13,27 1,20.5 1,7.5" fill="#ec1f27" stroke="#fff" stroke-width="1.5"/><circle cx="13" cy="12" r="4.5" fill="#fff"/><path d="M10 16l-1 5 4-2 4 2-1-5" fill="#fff"/></svg></li>
    <li>Annual Inspections<svg class="hex-icon" viewBox="0 0 26 28"><polygon points="13,1 25,7.5 25,20.5 13,27 1,20.5 1,7.5" fill="#ec1f27" stroke="#fff" stroke-width="1.5"/><rect x="8" y="8" width="10" height="12" fill="none" stroke="#fff" stroke-width="2"/></svg></li>
    <li>Pre-Use Inspections<svg class="hex-icon" viewBox="0 0 26 28"><polygon points="13,1 25,7.5 25,20.5 13,27 1,20.5 1,7.5" fill="#ec1f27" stroke="#fff" stroke-width="1.5"/><circle cx="13" cy="14" r="5" fill="none" stroke="#fff" stroke-width="2"/><circle cx="13" cy="14" r="1.8" fill="#fff"/></svg></li>
    <li>Training<svg class="hex-icon" viewBox="0 0 26 28"><polygon points="13,1 25,7.5 25,20.5 13,27 1,20.5 1,7.5" fill="#ec1f27" stroke="#fff" stroke-width="1.5"/><rect x="7" y="8" width="12" height="8" fill="none" stroke="#fff" stroke-width="2"/><line x1="13" y1="16" x2="13" y2="21" stroke="#fff" stroke-width="2"/></svg></li>
    <li>OPOS Document/Work Plan<svg class="hex-icon" viewBox="0 0 26 28"><polygon points="13,1 25,7.5 25,20.5 13,27 1,20.5 1,7.5" fill="#ec1f27" stroke="#fff" stroke-width="1.5"/><path d="M9 7h6l3 3v11H9z" fill="none" stroke="#fff" stroke-width="2"/></svg></li>
  </ul>
</main>
</body>
</html>
```